Merrill Law Group Social Media Design - Wordpress

I need
Circles
Friends
Videos
Updates
designs for a law firm in Anchorage, AK. In the project section that allows me to detail what I want and don't want, I will show you what one company has designed, that is so-so, but not what I wanted.
Uploads
Files beginning with CR have the feel I would like to emulate. All happy, light bright.
Files beginning with JC are what I don't want. I don't want any stock photos (i.e., the books) unless they are pictures of people. I also don't want any slogans or finger pointing. These files are also too white - white shirts, white-ish background, etc. I don't want to go crazy with color but would like more than is currently there. Our website is pelbridgelaw.example. We may re-design so it is up to you whether you want to coordinate with existing website vs. design social media independently.

Firm photos etc also attached. You may use stock photos of people representing clients if you would like. You may also photoshop firm pictures to improve if you see fit.
Thanks!

Target Market(s)

Clients who have been injured in auto accidents

Industry/Entity Type

Legal

Number of Pages Required

1 page

Font styles to use
Sans Serif

Requirements
Must have
• Would like designs for social media. Wordpress is what our website is done with. Looking for designs that convey happiness/warmth/light/hope without going overboard.
• Attached files that begin with CR have a look and feel that I would like to try to capture, but not copy. We currently don't have photographs that lend themselves to this particularly well. Maybe you can figure out a way to soften/warm up what we do have.
Nice to have
• Please feel free to use stock photos of people/families if you want to represent some clients in your design.
Should not have
• Clip art or slogans like the files beginning with JC. We do not like those.

```html
<!DOCTYPE html>
<html lang="en">
<head>
<meta charset="utf-8">
<title>Merrill Law Group</title>
<link href="https://fonts.googleapis.com/css2?family=Roboto:wght@300;400;500;700&family=Roboto+Condensed:wght@400;700&display=swap" rel="stylesheet">
<style>
:root{
  --navy:#0b1550;
  --navy-deep:#070f3d;
  --blog-blue:#2f3a7c;
  --form-blue:#283273;
  --heading-blue:#1d2d6e;
  --tan:#b8a678;
  --tan-light:#c9b98f;
  --text:#555a66;
  --muted:#8a8f99;
  --white:#ffffff;
  --black:#0a0a0a;
  --grey-band:#d9dbdf;
}
*{box-sizing:border-box;margin:0;padding:0}
html,body{width:1200px;height:3795px;overflow:hidden}
body{position:relative;font-family:"Roboto",Arial,sans-serif;color:var(--text);background:var(--white)}
.abs{position:absolute}
a{color:inherit;text-decoration:none}

/* header */
.site-header{left:0;top:0;width:1200px;height:139px;background:var(--white)}
.brand{left:74px;top:30px;display:flex;align-items:center;gap:14px}
.brand-mark{width:44px;height:44px;background:var(--navy)}
.brand-name{font-size:30px;line-height:31px;font-weight:500;color:var(--navy);letter-spacing:.5px;text-transform:uppercase}
.phone{left:614px;top:48px;display:flex;gap:12px;align-items:flex-start}
.phone-number{font-size:31px;font-weight:700;color:#333;line-height:32px}
.phone-sub{font-size:12px;color:var(--muted);margin-left:44px;margin-top:2px}
.socials{left:956px;top:50px;display:flex;gap:14px}
.social{width:40px;text-align:center;font-size:10px;font-weight:500;color:#333}
.social span{display:block;width:26px;height:26px;border-radius:50%;background:#2f3238;margin:0 auto 6px}

/* nav */
.main-nav{left:0;top:139px;width:1200px;height:56px;background:var(--navy)}
.main-nav ul{position:absolute;left:88px;top:0;display:flex;list-style:none;gap:24px;height:56px;align-items:center}
.main-nav li{font-family:"Roboto Condensed",Arial,sans-serif;font-size:14px;font-weight:700;color:var(--white);text-transform:uppercase}
.main-nav li.active{border-bottom:2px solid var(--white);padding-bottom:2px}
.eval-btn{left:898px;top:148px;width:278px;height:38px;background:var(--white);display:flex;align-items:center;justify-content:center;gap:14px;font-family:"Roboto Condensed",Arial,sans-serif;font-weight:700;font-size:14px;color:var(--navy);text-transform:uppercase}
.eval-btn i{width:18px;height:14px;border:2px solid var(--navy);display:block}

/* hero */
.hero{left:0;top:195px;width:1200px;height:468px;background:radial-gradient(ellipse at 50% 65%,#4a4d52 0%,#26282c 45%,#0e0f11 100%)}
.hero-title{left:0;top:268px;width:1200px;text-align:center;font-family:"Roboto Condensed",Arial,sans-serif;font-size:44px;line-height:56px;color:var(--white);text-transform:uppercase;letter-spacing:.5px}
.consult{left:520px;top:384px;width:160px;height:40px;border:2px solid var(--tan);color:var(--white);font-size:18px;text-transform:uppercase;display:flex;align-items:center;justify-content:center;background:rgba(0,0,0,.35)}
.hero-arrow{top:360px;width:30px;height:84px;background:rgba(120,120,120,.55)}
.hero-arrow.left{left:0}.hero-arrow.right{right:0}
.hero-dots{left:534px;top:648px;display:flex;gap:10px}
.hero-dots span{width:36px;height:3px;background:rgba(255,255,255,.35)}
.hero-dots span.on{background:var(--white)}

/* tan band */
.priority-band{left:0;top:663px;width:1200px;height:81px;background:var(--tan)}
.priority-text{left:90px;top:688px;font-size:22px;color:var(--white);font-weight:300}
.practices-btn{left:840px;top:683px;width:246px;height:40px;border:2px solid var(--white);color:var(--white);font-size:19px;font-weight:500;text-transform:uppercase;display:flex;align-items:center;justify-content:center}

/* intro */
.intro-heading{left:76px;top:774px;width:640px;font-size:22px;line-height:28px;font-weight:700;color:var(--heading-blue)}
.intro-body{left:76px;top:842px;width:650px;font-size:13px;line-height:16.5px;color:var(--text)}
.intro-body p{margin-bottom:16px}
.intro-photo{left:739px;top:744px;width:390px;height:430px;background:linear-gradient(160deg,#f4f1ea 0%,#d9cfbf 55%,#8d7a5e 100%)}

/* practice strip */
.strengths{left:0;top:1172px;width:1200px;height:461px;background:var(--navy)}
.strengths-title{left:0;top:1222px;width:1200px;text-align:center;font-size:25px;font-weight:700;color:var(--white)}
.strengths-rule{left:570px;top:1270px;width:60px;height:2px;background:var(--tan)}
.strength{top:1326px;width:300px;text-align:center;color:var(--white)}
.strength svg{display:block;margin:0 auto}
.strength h3{font-size:19px;font-weight:500;margin:24px 0 10px}
.strength p{font-size:11.5px;line-height:15px;padding:0 10px;height:48px}
.read-more{display:inline-block;margin-top:14px;border:1.5px solid var(--white);font-size:12px;padding:5px 22px}

/* attorneys */
.section-title{font-size:26px;font-weight:500;color:var(--heading-blue)}
.title-rule{width:108px;height:2px;background:var(--tan)}
.pager{display:flex;gap:6px}
.pager span{width:40px;height:30px;border:1.5px solid #7d8089;display:flex;align-items:center;justify-content:center}
.attorney-band{left:0;top:1826px;width:1200px;height:74px;background:var(--navy)}
.attorney{top:1757px;width:262px}
.attorney-photo{width:262px;height:312px}
.attorney h3{font-size:25px;font-weight:500;color:var(--heading-blue);margin:30px 0 8px}
.attorney p{font-size:12px;line-height:15px;color:var(--muted);width:250px}
.attorney .profile{display:block;margin-top:14px;font-size:13px;font-weight:500;color:var(--tan);text-transform:uppercase}

/* client questions */
.questions{left:0;top:2266px;width:1200px;height:241px;background:linear-gradient(180deg,#e4e6ea 0%,#cfd2d8 100%)}
.questions-text{left:76px;top:2360px;width:1050px;font-size:15.5px;line-height:23px;color:#8b8f98}
.questions-text a{color:var(--tan)}

/* blog */
.post{left:139px;width:988px;height:91px;background:var(--blog-blue);display:flex;align-items:center}
.post-date{width:52px;margin-left:16px;text-align:center}
.post-date b{display:block;background:var(--white);color:var(--navy);font-size:28px;font-weight:700;line-height:38px}
.post-date i{display:block;background:var(--tan);color:var(--white);font-style:normal;font-size:17px;font-weight:700;line-height:24px}
.post-body{margin-left:28px;width:860px;color:var(--white);font-size:11.5px;line-height:14px;font-style:italic}
.post-meta{margin-top:10px;font-style:normal;font-size:11px;color:#c8cbe0}
.divider{left:0;top:2962px;width:1200px;height:2px;background:var(--tan-light)}

/* evaluation */
.eval-copy{left:76px;top:3096px;width:470px;font-size:16px;line-height:26px;color:var(--muted)}
.inquiry{left:646px;top:3008px;width:483px;height:468px;background:var(--form-blue);color:var(--white);padding:26px 36px}
.inquiry h3{font-size:24px;font-weight:400}
.req{position:absolute;right:36px;top:36px;font-size:11px}
.field label{display:block;font-size:12px;font-weight:500;margin:16px 0 5px}
.field .input{height:38px;background:var(--white);font-size:11px;color:#9a9a9a;padding:12px 8px}
.field .area{height:108px}
.submit-row{display:flex;align-items:center;gap:18px;margin-top:18px}
.submit{width:210px;height:42px;border:2px solid var(--white);font-size:18px;font-weight:700;display:flex;align-items:center;justify-content:center}
.secure{font-size:11.5px;line-height:14px;display:flex;align-items:center;gap:10px}

/* footer */
.site-footer{left:0;top:3507px;width:1200px;height:288px;background:var(--black);color:#e8e8e8}
.footer-brand{left:492px;top:3530px;display:flex;align-items:center;gap:14px}
.footer-brand .brand-mark{background:var(--white);width:44px;height:44px}
.footer-brand .brand-name{color:var(--white)}
.footer-rule{left:420px;top:3600px;width:360px;height:1px;background:#555}
.footer-col{top:3618px;font-size:12px;line-height:16px}
.footer-socials{left:718px;top:3614px;display:flex;gap:10px;border-left:1px solid #555;padding-left:12px}
.footer-socials .social{color:#ddd;width:36px;font-size:9.5px}
.footer-socials .social span{background:#e8e8e8;width:22px;height:22px}
.footer-rule2{left:226px;top:3700px;width:750px;height:1px;background:#444}
.footer-nav{left:0;top:3712px;width:1200px;display:flex;justify-content:center;gap:20px;font-family:"Roboto Condensed",Arial,sans-serif;font-size:13px;font-weight:700;color:var(--white)}
.footer-legal{font-size:9px;color:#777;top:3768px}
</style>
</head>
<body>

<header class="site-header abs">
  <div class="brand abs"><span class="brand-mark"></span><div class="brand-name">Merrill<br>Law Group</div></div>
  <div class="phone abs">
    <svg width="30" height="30" viewBox="0 0 24 24"><path d="M6.6 10.8c1.4 2.8 3.8 5.1 6.6 6.6l2.2-2.2c.3-.3.7-.4 1-.2 1.1.4 2.3.6 3.6.6.6 0 1 .4 1 1V20c0 .6-.4 1-1 1C10.6 21 3 13.4 3 4c0-.6.4-1 1-1h3.5c.6 0 1 .4 1 1 0 1.3.2 2.5.6 3.6.1.3 0 .7-.2 1z" fill="var(--navy)"/></svg>
    <div><div class="phone-number">907-555-0142</div><div class="phone-sub" style="margin-left:0">Call Us For Free Consultation</div></div>
  </div>
  <div class="socials abs">
    <div class="social"><span></span>Circles</div>
    <div class="social"><span></span>Friends</div>
    <div class="social"><span></span>Videos</div>
    <div class="social"><span></span>Updates</div>
  </div>
</header>

<nav class="main-nav abs">
  <ul>
    <li class="active">Home</li><li>Attorneys</li><li>Blog</li><li>Resources</li><li>Practice Areas</li><li>FAQ</li><li>Client Questions</li><li>Contact Us</li>
  </ul>
</nav>
<a class="eval-btn abs"><i></i>Free Case Evaluation</a>

<section class="hero abs" role="img" aria-label="Group photo of the firm's attorneys in suits"></section>
<div class="hero-arrow left abs"></div>
<div class="hero-arrow right abs"></div>
<h1 class="hero-title abs">We have helped thousands of injury<br>victims like you</h1>
<a class="consult abs">Consult</a>
<div class="hero-dots abs"><span class="on"></span><span></span><span></span></div>

<div class="priority-band abs"></div>
<p class="priority-text abs">Getting your case dismissed is our top priority.</p>
<a class="practices-btn abs">Check Our Practices</a>

<h2 class="intro-heading abs">Our team does not promise you more than you deserve,<br>but we will not settle for less.</h2>
<div class="intro-body abs">
  <p>We help injured people just like you. If you have been injured in Alaska, we will work to get you full and fair compensation for your injuries. We will be available to help you every step of the way and we will work hard to get a good settlement in your case.</p>
  <p>We've helped thousands of people who were injured in accidents, and we know that an accident that results in injury can be a terrible and frightening experience. Traumatic injuries cause significant physical pain, but accident victims also have many other issues — medical bills to pay, car repairs to consider, lost wages to make up, and paperwork from the insurance company to fill out. We pride ourselves in taking a global approach to client service, and we work hard to help you with each and every issue and concern as you try to put your life back together.</p>
  <p>We also have seen enough of these cases to know that a big settlement doesn't solve all of your problems. However, settling too soon or for too little money can make those problems even worse. We work hard to get our clients as much money as possible to compensate them for their experience. Our experience in the insurance industry provides us with new perspective and insight into the methods and strategies of insurance companies. We use this knowledge, along with our reputation as willing and competent litigators, to convince insurance companies to pay our clients a fair settlement—one that represents full and fair compensation for the accident victim's ordeal.</p>
</div>
<div class="intro-photo abs" role="img" aria-label="Portrait of the lead attorney seated at his desk"></div>

<section class="strengths abs"></section>
<h2 class="strengths-title abs">Working With Excellent Attorneys</h2>
<div class="strengths-rule abs"></div>

<div class="strength abs" style="left:104px">
  <svg width="100" height="100" viewBox="0 0 100 100"><g fill="var(--tan)"><rect x="30" y="18" width="40" height="18" rx="3" transform="rotate(-20 50 27)"/><rect x="46" y="34" width="8" height="50" transform="rotate(-60 50 59)"/><rect x="12" y="80" width="40" height="8"/></g></svg>
  <h3>Practice Areas</h3>
  <p>Auto and Vehicle Accidents, Drunk Driving Accidents, Plane Crashes, Maritime Injuries, Motorcycle Accidents, Wrongful Death, Brain Injuries</p>
  <a class="read-more">Read More</a>
</div>
<div class="strength abs" style="left:450px">
  <svg width="100" height="100" viewBox="0 0 100 100"><g fill="var(--tan)"><circle cx="50" cy="32" r="18"/><path d="M18 90c0-20 14-34 32-34s32 14 32 34z"/></g><path d="M46 58l4 20 4-20z" fill="var(--navy)"/></svg>
  <h3>Resources</h3>
  <p>Brain Injury, Drunk Driving Accidents, Drug and Product Recalls, Disability Resources, Legal Dictionaries, Legal Search, Medical Products, Other Legal Reference Link</p>
  <a class="read-more">Read More</a>
</div>
<div class="strength abs" style="left:795px">
  <svg width="100" height="100" viewBox="0 0 100 100"><rect x="22" y="10" width="56" height="80" fill="none" stroke="var(--tan)" stroke-width="5"/><g fill="var(--tan)"><rect x="32" y="26" width="36" height="5"/><rect x="32" y="40" width="36" height="5"/><rect x="32" y="54" width="36" height="5"/><rect x="32" y="68" width="24" height="5"/></g></svg>
  <h3>Helpful Medical Articles</h3>
  <p>Brain Injury, Drunk Driving Accidents, Drug and Product Recalls, Disability Resources, Legal Dictionaries, Legal Search, Medical Products, Other Legal Reference Links</p>
  <a class="read-more">Read More</a>
</div>

<h2 class="section-title abs" style="left:76px;top:1658px">Meet the Attorneys</h2>
<div class="title-rule abs" style="left:76px;top:1706px"></div>
<div class="pager abs" style="left:1026px;top:1690px"><span><svg width="12" height="14"><path d="M9 2L3 7l6 5" stroke="#555" stroke-width="2" fill="none"/></svg></span><span><svg width="12" height="14"><path d="M3 2l6 5-6 5" stroke="#555" stroke-width="2" fill="none"/></svg></span></div>

<div class="attorney-band abs"></div>
<div class="attorney abs" style="left:112px">
  <div class="attorney-photo" role="img" aria-label="Portrait of attorney Thomas Merrill" style="background:linear-gradient(180deg,#f2f2f2,#cfd3da 60%,#2b3140)"></div>
  <h3>Thomas Merrill</h3>
  <p>Lorem ipsum dolor sit amet, consectetur adipiscing elit. Cras tincidunt hendrerit est ut porta. Donec id ipsum sed nibh egestas blandit. Curabitur sed libero molestie, placerat enim sed, tristique eros.</p>
  <a class="profile">View Attorney Profile</a>
</div>
<div class="attorney abs" style="left:485px">
  <div class="attorney-photo" role="img" aria-label="Portrait of attorney Evan Hale" style="background:linear-gradient(180deg,#1c1c1e,#3a3a3e 55%,#d8dbe2)"></div>
  <h3>Evan Hale</h3>
  <p>Lorem ipsum dolor sit amet, consectetur adipiscing elit. Cras tincidunt hendrerit est ut porta. Donec id ipsum sed nibh egestas blandit. Curabitur sed libero molestie, placerat enim sed, tristique eros.</p>
  <a class="profile">View Attorney Profile</a>
</div>
<div class="attorney abs" style="left:854px">
  <div class="attorney-photo" role="img" aria-label="Portrait of attorney Marco Reyes" style="background:linear-gradient(180deg,#16161a,#3b3635 55%,#7b7266)"></div>
  <h3>Marco Reyes</h3>
  <p>Lorem ipsum dolor sit amet, consectetur adipiscing elit. Cras tincidunt hendrerit est ut porta. Donec id ipsum sed nibh egestas blandit. Curabitur sed libero molestie, placerat enim sed, tristique eros.</p>
  <a class="profile">View Attorney Profile</a>
</div>

<section class="questions abs" role="img" aria-label="Faded photo of a city street behind the client questions"></section>
<h2 class="section-title abs" style="left:76px;top:2294px">Client Questions</h2>
<div class="title-rule abs" style="left:76px;top:2340px"></div>
<div class="pager abs" style="left:1026px;top:2296px"><span><svg width="12" height="14"><path d="M9 2L3 7l6 5" stroke="#555" stroke-width="2" fill="none"/></svg></span><span><svg width="12" height="14"><path d="M3 2l6 5-6 5" stroke="#555" stroke-width="2" fill="none"/></svg></span></div>
<p class="questions-text abs">Lorem ipsum dolor sit amet, consectetur adipiscing elit. Cras tincidunt hendrerit est ut porta. Donec id ipsum sed nibh egestas blandit. Curabitur sed libero molestie, placerat enim sed, tristique eros. Vivamus ac risus ac nisl fringilla lobortis sed eu velit. Interdum et malesuada fames ac ante ipsum primis in faucibus. Pellentesque euismod condimentum quam eu porta. Donec dictum, felis at dignissim laoreet, erat arcu bibendum augue, in tincidunt mi velit in tellus. <a>Read More...</a></p>

<h2 class="section-title abs" style="left:76px;top:2524px">Read our expertly written blog</h2>
<div class="title-rule abs" style="left:76px;top:2572px"></div>

<article class="post abs" style="top:2613px">
  <div class="post-date"><b>21</b><i>JUL</i></div>
  <div class="post-body">"Lorem ipsum dolor sit amet, consectetur adipiscing elit. Cras tincidunt hendrerit est ut porta. Donec id ipsum sed nibh egestas blandit. Curabitur sed libero molestie, placerat enim sed, tristique eros. Vivamus ac risus ac nisl fringilla lobortis sed eu velit. Interdum et malesuada fames ac ante ipsum primis in faucibus."<div class="post-meta">◷ in Case Updates, Client Forms</div></div>
</article>
<article class="post abs" style="top:2724px">
  <div class="post-date"><b>26</b><i>JUL</i></div>
  <div class="post-body">"Lorem ipsum dolor sit amet, consectetur adipiscing elit. Cras tincidunt hendrerit est ut porta. Donec id ipsum sed nibh egestas blandit. Curabitur sed libero molestie, placerat enim sed, tristique eros. Vivamus ac risus ac nisl fringilla lobortis sed eu velit. Interdum et malesuada fames ac ante ipsum primis in faucibus."<div class="post-meta">◷ in Case Updates, Client Forms</div></div>
</article>
<article class="post abs" style="top:2836px">
  <div class="post-date"><b>29</b><i>JUL</i></div>
  <div class="post-body">"Lorem ipsum dolor sit amet, consectetur adipiscing elit. Cras tincidunt hendrerit est ut porta. Donec id ipsum sed nibh egestas blandit. Curabitur sed libero molestie, placerat enim sed, tristique eros. Vivamus ac risus ac nisl fringilla lobortis sed eu velit. Interdum et malesuada fames ac ante ipsum primis in faucibus."<div class="post-meta">◷ in Case Updates, Client Forms</div></div>
</article>

<div class="divider abs"></div>

<h2 class="section-title abs" style="left:76px;top:3010px">Free Case Evaluation</h2>
<div class="title-rule abs" style="left:76px;top:3058px"></div>
<p class="eval-copy abs">Lorem ipsum dolor sit amet, consectetur adipiscing elit. Cras tincidunt hendrerit est ut porta. Donec id ipsum sed nibh egestas blandit. Curabitur sed libero molestie, placerat enim sed, tristique eros. Vivamus ac risus ac nisl fringilla lobortis sed eu velit. Interdum et malesuada fames ac ante ipsum primis in faucibus. Pellentesque euismod condimentum quam eu porta. Donec dictum, felis at dignissim laoreet, erat arcu bibendum augue, in tincidunt mi velit in tellus. Etiam mattis arcu sed sapien dictum, sed vestibulum diam fermentum. Nam fringilla erat at tellus ultrices eleifend. Suspendisse non tortor condimentum lorem facilisis tincidunt at quis neque.</p>

<form class="inquiry abs">
  <h3>Inquiry Form</h3>
  <span class="req">*Required Fields</span>
  <div class="field"><label>Name:*</label><div class="input">Insert your name and last name</div></div>
  <div class="field"><label>Phone:</label><div class="input">Insert your telephone number</div></div>
  <div class="field"><label>Email:*</label><div class="input">Insert your email address</div></div>
  <div class="field"><label>How can we help you?:</label><div class="input area">Case details</div></div>
  <div class="submit-row">
    <div class="submit">SUBMIT</div>
    <div class="secure"><svg width="26" height="30" viewBox="0 0 26 30"><path d="M7 13V9a6 6 0 0112 0v4" stroke="#fff" stroke-width="3" fill="none"/><rect x="3" y="13" width="20" height="15" fill="#fff"/></svg><span>We never share your info<br>secure and Confidential.</span></div>
  </div>
</form>

<footer class="site-footer abs"></footer>
<div class="footer-brand abs"><span class="brand-mark"></span><div class="brand-name">Merrill<br>Law Group</div></div>
<div class="footer-rule abs"></div>
<div class="footer-col abs" style="left:282px">Merrill Law Group<br>410 B St<br>Anchorage, AK 99501</div>
<div class="footer-col abs" style="left:444px;border-left:1px solid #555;padding-left:12px">Email Address: thomas@pelbridgelaw.example<br>Phone: (907) 555-0142<br>Fax: (907) 555-0187</div>
<div class="footer-socials abs">
  <div class="social"><span></span>Circles</div>
  <div class="social"><span></span>Friends</div>
  <div class="social"><span></span>Videos</div>
  <div class="social"><span></span>Updates</div>
</div>
<div class="footer-rule2 abs"></div>
<ul class="footer-nav abs" style="list-style:none">
  <li>HOME</li><li>ATTORNEYS</li><li>BLOG</li><li>RESOURCES</li><li>PRACTICE AREAS</li><li>FAQ</li><li>CLIENT QUESTIONS</li><li>CONTACT US</li>
</ul>
<div class="footer-legal abs" style="left:72px">Copyright © 2016 All rights reserved</div>
<div class="footer-legal abs" style="left:1010px">Terms &amp; Conditions &nbsp;|&nbsp; Privacy Policy</div>

</body>
</html>
```